Quorvix Letter head

Quorvix is a young and energetic software development consultancy. We spend our time working with clients to turn what ever is in their heads in to software.
We are trying to create an image of a high class software boutique who build class leading bespoke solutions.
We need a sharp letter head that looks great on high quality media.
We like bold colours and distinctive design. So show us what you can do.
Industry/Entity Type
Software
Requirements
Must have
- Our company is based in the UK and are requried to have on the paper somewhere the following information:
* Registered company name: Quorvix Ltd
* Registered company number
* VAT registration number
In addition we also want the following:
* An email address
* Telephone number
* Website address
An example of what some pages have in their footer is something like the following:
Quorvix Ltd is registered in England and Wales. Reg. no: 5316274
Registered office: 48 Cobblewick Road, Harlow Essex, CM93TP. Tel: 07712365081
You do not have to use this sentance but please make sure your design incorporates accommodates the requirements for UK based companies

```html
<!DOCTYPE html>
<html lang="en">
<head>
<meta charset="UTF-8">
<title>Quorvix Letterhead</title>
<link href="https://fonts.googleapis.com/css2?family=Marcellus&display=swap" rel="stylesheet">
<style>
  :root {
    --brand-red: #c3202f;
    --paper: #ffffff;
    --ink: #3a3a3a;
    --muted: #7a7a7a;
    --rule: #c9c9c9;
    --faint-mark: #dcd7d7;
  }
  * { margin: 0; padding: 0; box-sizing: border-box; }
  html, body {
    width: 971px;
    height: 1200px;
    overflow: hidden;
    background: var(--paper);
  }
  .letterhead {
    position: relative;
    width: 971px;
    height: 1200px;
    background: var(--paper);
    font-family: "Marcellus", serif;
    color: var(--ink);
  }
  .brand-name {
    position: absolute;
    left: 83px;
    top: 62px;
    font-size: 74px;
    line-height: 1;
    letter-spacing: 1px;
    color: var(--brand-red);
    text-transform: uppercase;
  }
  .header-rule {
    position: absolute;
    left: 540px;
    top: 73px;
    width: 1px;
    height: 55px;
    background: var(--rule);
  }
  .address {
    position: absolute;
    left: 572px;
    top: 74px;
    font-size: 14px;
    line-height: 16px;
    font-style: normal;
    color: var(--ink);
  }
  .website {
    position: absolute;
    left: 572px;
    top: 110px;
    font-size: 17px;
    letter-spacing: 1px;
    color: var(--brand-red);
  }
  .contact-tab {
    position: absolute;
    left: 769px;
    width: 202px;
    height: 23px;
    background: var(--brand-red);
    border-radius: 5px 0 0 5px;
    color: #fff;
    font-size: 14px;
    line-height: 23px;
    display: flex;
    align-items: center;
    gap: 6px;
    white-space: nowrap;
  }
  .contact-tab svg { width: 13px; height: 13px; flex: none; }
  .contact-tab--phone { top: 75px; padding-left: 40px; }
  .contact-tab--email { top: 102px; padding-left: 14px; }
  .footer-mark {
    position: absolute;
    left: 0;
    right: 0;
    top: 1088px;
    text-align: center;
    font-size: 84px;
    line-height: 1;
    letter-spacing: 4px;
    color: var(--faint-mark);
    text-transform: uppercase;
  }
  .legal-line {
    position: absolute;
    left: 0;
    right: 0;
    top: 1182px;
    text-align: center;
    font-size: 11px;
    line-height: 12px;
    color: var(--muted);
    letter-spacing: 0.3px;
    white-space: nowrap;
  }
</style>
</head>
<body>
  <main class="letterhead">
    <header>
      <div class="brand-name">Quorvix</div>
      <div class="header-rule"></div>
      <address class="address">
        10000 Quorvix Bldg,<br>Cityname, Countryname
      </address>
      <div class="website">www.quorvix.com</div>
      <div class="contact-tab contact-tab--phone">
        <svg viewBox="0 0 16 16" aria-hidden="true"><circle cx="8" cy="8" r="7.5" fill="#fff"/><path d="M5.2 4.2l1.4-.4 1 2.2-.9.7c.4 1 1.2 1.8 2.2 2.2l.7-.9 2.2 1-.4 1.4c-3.2.2-6.4-3-6.2-6.2z" fill="#c3202f"/></svg>
        <span>020-555-0148</span>
      </div>
      <div class="contact-tab contact-tab--email">
        <svg viewBox="0 0 16 16" aria-hidden="true"><rect x="1.5" y="3.5" width="13" height="9" rx="1" fill="none" stroke="#fff" stroke-width="1.4"/><path d="M2 4.5l6 4.5 6-4.5" fill="none" stroke="#fff" stroke-width="1.4"/></svg>
        <span>info@quorvix.com</span>
      </div>
    </header>
    <footer>
      <div class="footer-mark">Quorvix</div>
      <p class="legal-line">Quorvix Ltd is registered in England and Wales. Reg. no: 5316274 &middot; VAT reg. no: GB 294 7183 56 &middot; Registered office: 48 Cobblewick Road, Harlow Essex, CM93TP</p>
    </footer>
  </main>
</body>
</html>
```